Business Card for Willowcrest Terrain Advisors

We need a business card for Willowcrest Terrain Advisors. The company website address is provided below. The company logo is attached. We provide specialized permafrost services to the mining, transportation, and oil & gas industries. The card should be prepared for:
Dominic Halloway, PhD.
Willowcrest Terrain Advisors
PO Box 418529
Birch Hollow, Alaska 99612
Direct: +1-907-555-2964
Email: dhalloway@terrainadvisors-example.com
Website: www.willowcrestterrainadvisors-example.com

```html
<!DOCTYPE html>
<html lang="en">
<head>
<meta charset="utf-8">
<title>Willowcrest Terrain Advisors – Business Card</title>
<link href="https://fonts.googleapis.com/css2?family=Jost:wght@400;500;600;700&display=swap" rel="stylesheet">
<style>
  :root {
    --page-bg: #e9e6e1;
    --ink: #18222d;
    --ink-soft: #3a4653;
    --muted: #5d6a75;
    --sky-top: #6f8fc0;
    --sky-mid: #c9d6e6;
    --cloud: #eef2f7;
    --treeline: #4d6b3f;
    --ground: #8d9773;
    --gravel: #9a9a8e;
    --rule: #2b3540;
  }
  * { box-sizing: border-box; margin: 0; padding: 0; }
  html, body {
    width: 1200px; height: 900px; overflow: hidden;
    background: var(--page-bg);
    font-family: "Jost", "Futura", sans-serif;
    color: var(--ink);
  }
  .sheet { position: relative; width: 1200px; height: 900px; }

  .card {
    position: absolute;
    width: 665px; height: 380px;
    border-radius: 34px;
    overflow: hidden;
    box-shadow: 0 10px 28px rgba(0,0,0,0.22);
  }
  .card--front { left: 70px; top: 50px; }
  .card--back  { left: 465px; top: 470px; }

  .card__photo {
    position: absolute; inset: 0;
    background:
      linear-gradient(180deg,
        var(--sky-top) 0%,
        var(--sky-mid) 30%,
        var(--cloud) 48%,
        var(--sky-mid) 60%,
        var(--treeline) 68%,
        var(--ground) 80%,
        var(--gravel) 100%);
  }

  .brand-name {
    position: absolute;
    font-weight: 600;
    color: var(--ink);
    letter-spacing: 0.02em;
    white-space: nowrap;
  }
  .card--front .brand-name {
    left: 70px; top: 120px;
    font-size: 40px;
  }

  .holder {
    position: absolute; left: 34px; top: 40px;
  }
  .holder__name {
    font-weight: 700; font-size: 20px;
    letter-spacing: 0.01em;
    text-transform: uppercase;
    color: var(--ink);
  }
  .holder__company {
    font-weight: 400; font-size: 16px;
    color: var(--muted);
    margin-top: 2px;
  }

  .contact {
    position: absolute; left: 250px; top: 112px;
    list-style: none;
  }
  .contact__item {
    display: flex; align-items: center; gap: 8px;
    font-size: 15px; font-weight: 400;
    color: var(--ink);
    line-height: 26px;
    white-space: nowrap;
  }
  .contact__icon { width: 14px; height: 14px; flex: none; }

  .divider {
    position: absolute; left: 250px; top: 232px;
    width: 385px; height: 1.5px;
    background: var(--rule);
  }
  .card--back .brand-name {
    left: 250px; top: 246px;
    font-size: 28px;
  }
</style>
</head>
<body>
<main class="sheet">

  <section class="card card--front" aria-label="Card front">
    <div class="card__photo" role="img" aria-label="Photograph of an Alaskan field site with a row of steel pipes under a cloudy sky above a treeline"></div>
    <p class="brand-name">Willowcrest Terrain Advisors</p>
  </section>

  <section class="card card--back" aria-label="Card back">
    <div class="card__photo" role="img" aria-label="Photograph of a row of steel pipes across a gravel pad with clouds and a treeline behind"></div>

    <div class="holder">
      <h1 class="holder__name">Dominic Halloway, PhD</h1>
      <p class="holder__company">Willowcrest Terrain Advisors</p>
    </div>

    <ul class="contact">
      <li class="contact__item">
        <svg class="contact__icon" viewBox="0 0 24 24" aria-hidden="true"><path fill="currentColor" d="M6.6 10.8a15.1 15.1 0 0 0 6.6 6.6l2.2-2.2a1 1 0 0 1 1-.25 11.4 11.4 0 0 0 3.6.57 1 1 0 0 1 1 1V20a1 1 0 0 1-1 1A17 17 0 0 1 3 4a1 1 0 0 1 1-1h3.5a1 1 0 0 1 1 1c0 1.25.2 2.45.57 3.57a1 1 0 0 1-.25 1z"/></svg>
        +1-907-555-2964
      </li>
      <li class="contact__item">
        <svg class="contact__icon" viewBox="0 0 24 24" aria-hidden="true"><path fill="currentColor" d="M3 5h18v14H3zm2 2v.5l7 4.5 7-4.5V7zm0 2.8V17h14V9.8l-7 4.5z"/></svg>
        dhalloway@terrainadvisors-example.com
      </li>
      <li class="contact__item">
        <svg class="contact__icon" viewBox="0 0 24 24" aria-hidden="true"><circle cx="12" cy="12" r="9" fill="none" stroke="currentColor" stroke-width="2"/><path d="M3 12h18M12 3c3 3.2 3 14.8 0 18M12 3c-3 3.2-3 14.8 0 18" fill="none" stroke="currentColor" stroke-width="1.6"/></svg>
        www.willowcrestterrainadvisors-example.com
      </li>
      <li class="contact__item">
        <svg class="contact__icon" viewBox="0 0 24 24" aria-hidden="true"><path fill="currentColor" d="M12 2a7 7 0 0 0-7 7c0 5 7 13 7 13s7-8 7-13a7 7 0 0 0-7-7zm0 9.5A2.5 2.5 0 1 1 12 6.5a2.5 2.5 0 0 1 0 5z"/></svg>
        PO Box 418529, Birch Hollow, Alaska 99612
      </li>
    </ul>

    <div class="divider"></div>
    <p class="brand-name">Willowcrest Terrain Advisors</p>
  </section>

</main>
</body>
</html>
```